Sproutwell

I need a product label that will be adhered to a square cardboard box. The label should be 8 inches by 8 inches. Contained within the box is a pot derived from 100% sustainable CocoCoir, a soil mix comprised of CocoCoir and Humus Compost, along with the plant drip tray. The brand name for the product is Fern4Home. I have attached a rough markup for an example

```html
<!DOCTYPE html>
<html lang="en">
<head>
<meta charset="utf-8">
<title>Sproutwell Container Garden Kit Label</title>
<link href="https://fonts.googleapis.com/css2?family=Archivo+Black&family=Barlow:wght@600;700&family=Barlow+Semi+Condensed:wght@600;700&display=swap" rel="stylesheet">
<style>
  :root {
    --bg: #d9e7b4;
    --bg-soft: #cfe0a4;
    --deep-green: #1d6b35;
    --brand-green: #2e9b2c;
    --lime: #8cc21f;
    --kraft: #e8d3b0;
    --kraft-dark: #d9bd92;
    --brown: #6b3f16;
    --ink: #2a211a;
    --badge-gold: #f2c81a;
    --badge-green: #3f8f2a;
  }
  * { margin: 0; padding: 0; box-sizing: border-box; }
  html, body { width: 1200px; height: 1200px; overflow: hidden; }
  body { background: var(--bg); font-family: "Barlow", sans-serif; }
  .label { position: relative; width: 1200px; height: 1200px; overflow: hidden; background: var(--bg); }

  .backdrop-art {
    position: absolute; left: 190px; top: 60px; width: 760px; height: 1020px;
    background: radial-gradient(ellipse at 50% 40%, var(--bg-soft) 0%, rgba(207,224,164,0.5) 55%, rgba(217,231,180,0) 75%);
  }

  .stamp {
    position: absolute; left: 25px; top: 34px; width: 373px; height: 166px;
    background: linear-gradient(135deg, #f2e4c8, var(--kraft) 60%, var(--kraft-dark));
    border: 3px dotted #b9a27c;
  }
  .stamp-title {
    position: absolute; left: 55px; top: 24px;
    font-family: "Barlow Semi Condensed", sans-serif; font-weight: 700;
    font-size: 50px; line-height: 58px; color: var(--brown); letter-spacing: 1px;
  }

  .brand-name {
    position: absolute; left: 0; width: 1200px; top: 300px; text-align: center;
    font-family: "Archivo Black", sans-serif; font-size: 132px; line-height: 180px;
    color: var(--brand-green); letter-spacing: 2px;
  }
  .tagline {
    position: absolute; left: 0; width: 1200px; top: 506px; text-align: center;
    font-family: "Barlow Semi Condensed", sans-serif; font-weight: 700;
    font-size: 40px; color: var(--deep-green);
  }

  .feature { position: absolute; text-align: center; width: 140px; }
  .feature svg { display: block; margin: 0 auto; }
  .feature-label {
    font-family: "Barlow Semi Condensed", sans-serif; font-weight: 700;
    font-size: 14px; line-height: 16px; color: var(--deep-green); margin-top: 8px;
  }
  .feature-label.large { font-size: 18px; }

  .kit-tag { position: absolute; left: 0; top: 876px; }
  .kit-list { position: absolute; left: 84px; top: 888px; color: var(--ink); }
  .kit-heading { font-weight: 700; font-size: 36px; line-height: 44px; color: #3a2a1c; }
  .kit-item { font-weight: 600; font-size: 23px; line-height: 30px; }

  .instructions {
    position: absolute; left: 81px; top: 1128px;
    font-weight: 600; font-size: 23px; color: #111;
  }

  .product-photo { position: absolute; left: 0; top: 0; }
</style>
</head>
<body>
<main class="label">
  <div class="backdrop-art" role="img" aria-label="Faint line drawing of a flowering plant in a woven pot"></div>

  <div class="stamp">
    <p class="stamp-title">CONTAINER<br>GARDEN KIT</p>
  </div>

  <h1 class="brand-name">SPROUTWELL</h1>
  <p class="tagline">ECO-FRIENDLY SUSTAINABLE CONTAINER GARDEN</p>

  <div class="feature" style="left:83px; top:711px;">
    <svg width="106" height="106" viewBox="0 0 106 106" aria-hidden="true">
      <circle cx="53" cy="53" r="49" fill="none" stroke="var(--deep-green)" stroke-width="5"/>
      <path d="M38 28q-5 6 0 12q5 6 0 12M53 28q-5 6 0 12q5 6 0 12M68 28q-5 6 0 12q5 6 0 12" fill="none" stroke="var(--deep-green)" stroke-width="2"/>
      <line x1="25" y1="56" x2="81" y2="56" stroke="var(--deep-green)" stroke-width="2"/>
      <line x1="25" y1="63" x2="81" y2="63" stroke="var(--deep-green)" stroke-width="2" stroke-dasharray="3 3"/>
      <path d="M38 70q-5 8 0 12q5-4 0-12M53 70q-5 8 0 12q5-4 0-12M68 70q-5 8 0 12q5-4 0-12" fill="none" stroke="var(--deep-green)" stroke-width="2"/>
    </svg>
    <p class="feature-label">WATER RETENTION<br>BREATHABLE</p>
  </div>

  <div class="feature" style="left:203px; top:708px;">
    <svg width="106" height="106" viewBox="0 0 106 106" aria-hidden="true">
      <circle cx="53" cy="53" r="49" fill="none" stroke="var(--deep-green)" stroke-width="5"/>
      <path d="M47 24h12v22l14 30h-40l14-30z" fill="none" stroke="var(--deep-green)" stroke-width="2"/>
      <path d="M38 64h30l5 12h-40z" fill="var(--deep-green)"/>
      <line x1="20" y1="86" x2="86" y2="20" stroke="var(--deep-green)" stroke-width="5"/>
    </svg>
    <p class="feature-label">NON-TOXIC</p>
  </div>

  <div class="feature" style="left:325px; top:705px;">
    <svg width="108" height="108" viewBox="0 0 108 108" aria-hidden="true">
      <circle cx="54" cy="54" r="50" fill="none" stroke="var(--deep-green)" stroke-width="5"/>
      <path d="M54 66v-34" stroke="var(--deep-green)" stroke-width="3"/>
      <ellipse cx="44" cy="40" rx="10" ry="5" fill="var(--lime)"/>
      <ellipse cx="64" cy="34" rx="10" ry="5" fill="var(--lime)"/>
      <path d="M22 64q16-4 32 4q14 6 32-6v8q-18 12-34 6q-16-6-30-4z" fill="var(--lime)"/>
    </svg>
    <p class="feature-label large">ECO-FRIENDLY</p>
  </div>

  <svg class="kit-tag" width="490" height="225" viewBox="0 0 490 225" aria-hidden="true">
    <defs>
      <linearGradient id="kraftFill" x1="0" y1="0" x2="1" y2="1">
        <stop offset="0" stop-color="#e9d2ac"/>
        <stop offset="1" stop-color="#d4b68a"/>
      </linearGradient>
    </defs>
    <path d="M60 4h418v218h-418l-56-56v-106z" fill="url(#kraftFill)"/>
    <circle cx="44" cy="113" r="14" fill="var(--bg)"/>
  </svg>

  <div class="kit-list">
    <p class="kit-heading">This Kit Includes:</p>
    <p class="kit-item">12″ Eco-Friendly Coco Coir Pot - 1</p>
    <p class="kit-item">1 cubic foot of potting soil mix - 1</p>
    <p class="kit-item">Packets of Balanced Plant Food - 4</p>
    <p class="kit-item">8oz Bottle of ROOTRA™ - 1</p>
    <p class="kit-item">Frip Tray - 1</p>
  </div>

  <p class="instructions">With easy to grow instructions</p>

  <svg class="product-photo" width="1200" height="1200" viewBox="0 0 1200 1200">
    <defs>
      <radialGradient id="photoTone" cx="0.55" cy="0.5" r="0.6">
        <stop offset="0" stop-color="#f4f3ea"/>
        <stop offset="0.5" stop-color="#b9cf8e"/>
        <stop offset="1" stop-color="#5f8a3a"/>
      </radialGradient>
    </defs>
    <circle cx="1070" cy="1010" r="320" fill="var(--lime)"/>
    <circle cx="1085" cy="1015" r="300" fill="url(#photoTone)" role="img" aria-label="Photo of a hand holding a young green plant in a coco coir pot"/>
    <g aria-hidden="true">
      <circle cx="866" cy="795" r="98" fill="var(--badge-gold)"/>
      <circle cx="866" cy="795" r="84" fill="var(--badge-green)"/>
      <circle cx="866" cy="795" r="64" fill="#ffffff"/>
    </g>
  </svg>
</main>
</body>
</html>
```